Software company WebSite Design (enterprise level SW, Mobile apps, HW prototypes)

We need design for our new webpages. We got new logo and new business cards and we need webdesign which will be match with those two.
We are dealing with corporate level software development - enterprise level portals, development of optimalization SW, route planning optimalizations. For a few months we are developing mobile applications for companies.
IMPORTANT is to express the cutting edge technological company.

Target Market(s)

IT company customers

Industry/Entity Type

Business

Number of Pages Required

2 page

Requirements
Must have
• Project needs to have landing page and product detail page. Design needs to be created including full font and example images as there would be a real webpage. Design should be clean, modern and expressing hi-tech level of the company.
• Example of well designer web pages - www.quorvelt.com, www.brandissa.com - We like the font formatting and font designs (colors, placing, etc - its professional).
• Attached image contains screenshot from old web landing page. It contains basic sections of our business (Simulation Tools, Enterprise Intranet Systems, Hi-tech web presentations, Supporting Enterprise services - Optimalization and logistics monitoring)

```html
<!DOCTYPE html>
<html lang="en">
<head>
<meta charset="utf-8">
<title>Kovrix Solutions</title>
<link href="https://fonts.googleapis.com/css2?family=Open+Sans:wght@400;600;700&family=Roboto+Condensed:wght@300;400;700&display=swap" rel="stylesheet">
<style>
:root{
  --accent:#3ec4f5;
  --ink:#333;
  --muted:#777;
  --rule:#ccc;
  --hero:#16181c;
  --footer:#242424;
  --footer-deep:#1a1a1a;
  --footer-text:#a8a8a8;
  --grey-panel:#e5e5e5;
  --white:#fff;
}
*{margin:0;padding:0;box-sizing:border-box}
html,body{width:1200px;height:3209px;overflow:hidden;background:var(--white)}
body{font-family:"Open Sans",Arial,sans-serif;color:var(--ink);font-size:12px}
.page{position:relative;width:1200px;height:3209px;overflow:hidden}
.abs{position:absolute}

/* hero */
.hero{left:0;top:0;width:1200px;height:562px;background:radial-gradient(ellipse at 45% 40%,#3a3d44 0%,#1d1f24 55%,#0d0e10 100%)}
.hero-visual{left:600px;top:100px;width:420px;height:462px;background:radial-gradient(ellipse at 55% 45%,rgba(120,110,105,.35) 0%,rgba(60,60,66,.2) 45%,rgba(20,20,24,0) 75%)}
.topbar{left:0;top:0;width:1200px;height:36px;background:rgba(0,0,0,.55)}
.social{top:10px;width:14px;height:14px;border:1px solid #888}
.topbar-info{top:9px;color:#ddd;font-size:11px}
.brand{left:171px;top:48px;height:44px;display:flex;align-items:center;gap:10px;color:#fff;font-family:"Roboto Condensed",sans-serif;font-weight:700;font-size:30px;letter-spacing:1px;background:rgba(0,0,0,.35);padding:0 12px}
.brand-mark{width:30px;height:30px;background:var(--accent)}
.nav{top:63px;left:570px;display:flex;gap:26px;color:#fff;font-size:11px;text-transform:uppercase}
.nav span.active{color:var(--accent)}
.hero-kicker{left:194px;top:236px;font-family:"Roboto Condensed",sans-serif;font-weight:300;font-size:40px;color:var(--accent)}
.hero-title{left:192px;top:282px;font-family:"Roboto Condensed",sans-serif;font-weight:700;font-size:58px;color:var(--accent)}
.read-more{left:194px;top:390px;font-size:10px;color:var(--accent);text-transform:uppercase;border-bottom:2px solid var(--accent);padding-bottom:6px}
.slide-dot{left:1168px;width:8px;height:8px;border:1px solid #aaa}

/* headings */
.section-title{left:0;width:1200px;text-align:center;font-family:"Roboto Condensed",sans-serif;font-weight:400;font-size:27px;color:var(--accent);text-transform:uppercase}
.divider{left:545px;width:110px;height:10px}

/* services */
.service{width:280px;height:166px}
.service h3{font-family:"Open Sans",sans-serif;font-weight:400;font-size:16px;text-align:center;text-transform:uppercase;padding-top:22px;padding-bottom:14px;border-bottom:1px solid #ddd;position:relative}
.service h3::after{content:"";position:absolute;left:138px;bottom:-3px;width:5px;height:5px;border-radius:50%;background:var(--accent)}
.service p{position:absolute;left:84px;top:82px;width:180px;font-size:10.5px;line-height:16px;color:#555}
.service svg{position:absolute;left:16px;top:88px}
.service.featured{background:var(--accent);color:#fff;box-shadow:0 4px 14px rgba(0,0,0,.25)}
.service.featured h3{border-color:rgba(255,255,255,.6)}
.service.featured h3::after{background:#fff}
.service.featured p{color:#fff}

/* about */
.video{left:160px;top:1166px;width:428px;height:267px;background:linear-gradient(180deg,#8d8f94 0%,#5a5d63 60%,#2e3033 100%)}
.about-lead{left:620px;top:1172px;font-size:14px;font-weight:600;color:#222}
.about-text{left:620px;width:420px;font-size:10.5px;line-height:18px;color:#555}
.about-item{padding-left:24px}
.about-item::before{content:"";position:absolute;left:2px;top:5px;width:9px;height:6px;border-left:2px solid #777;border-bottom:2px solid #777;transform:rotate(-45deg)}

/* stats */
.stats{left:0;top:1487px;width:1200px;height:186px;background:linear-gradient(90deg,#1c1d20,#2b2d31 50%,#1c1d20)}
.stat{width:180px;text-align:center;color:#fff}
.stat-ring{width:128px;height:128px;margin:0 auto;border-radius:50%;border:3px solid #fff;display:flex;align-items:center;justify-content:center;box-shadow:inset 0 0 0 6px rgba(0,0,0,.4),inset 0 0 0 8px #fff}
.stat-ring b{font-family:"Roboto Condensed",sans-serif;font-size:32px;font-weight:700}
.stat-label{font-size:11px;text-transform:uppercase;margin-top:6px}

/* process */
.process-line{left:261px;top:1877px;width:674px;height:2px;background:#555}
.step{width:120px;text-align:center}
.step-circle{width:76px;height:76px;margin:0 auto;border-radius:50%;border:2px solid #555;background:#fff;display:flex;align-items:center;justify-content:center;font-family:"Roboto Condensed",sans-serif;font-weight:300;font-size:30px;color:#555}
.step.current .step-circle{background:var(--accent);border-color:var(--accent);color:#fff}
.step-label{margin-top:14px;font-size:11px;text-transform:uppercase}

/* testimonial */
.testimonial-photo{left:0;top:1994px;width:599px;height:438px;background:linear-gradient(135deg,#5a5a5a 0%,#2f2f2f 60%,#1e1e1e 100%)}
.testimonial-frame{left:66px;top:2068px;width:467px;height:292px;border:2px solid #ccc;color:#fff;padding:70px 32px 0}
.testimonial-frame h2{font-family:"Roboto Condensed",sans-serif;font-weight:400;font-size:31px;text-transform:uppercase;margin-bottom:18px}
.testimonial-frame p{font-size:12px;line-height:17px}
.testimonial-side{left:599px;top:1994px;width:601px;height:438px;background:var(--grey-panel)}
.avatar{left:837px;top:2069px;width:106px;height:106px;border-radius:50%;background:radial-gradient(circle at 50% 40%,#c97f5e,#7a4130);border:3px solid #fff}
.quote{left:690px;top:2198px;width:420px;text-align:center;font-size:10.5px;line-height:17px;color:#444}
.quote-author{left:690px;top:2290px;width:420px;text-align:center;font-size:10px;font-style:italic;color:#555}
.bullet{height:3px;width:14px;background:#555}

/* clients */
.client{width:160px;top:2592px;display:flex;flex-direction:column;align-items:center;gap:8px;color:#555;font-weight:700;font-size:15px}
.client i{display:block;width:40px;height:40px;border-radius:50%;background:#666}

/* newsletter */
.newsletter{left:0;top:2753px;width:1200px;height:137px;background:var(--accent)}
.nl-title{left:237px;top:2798px;font-size:19px;font-weight:600;text-transform:uppercase;color:#fff}
.nl-sub{left:237px;top:2830px;font-size:11px;color:#fff;opacity:.9}
.nl-input{left:588px;top:2806px;width:278px;height:34px;border:1px solid #fff;font-size:10px;padding:10px;text-transform:uppercase;color:#fff}
.nl-button{left:898px;top:2802px;width:112px;height:42px;border-top:1px solid #fff;border-bottom:1px solid #fff;font-size:11px;text-transform:uppercase;text-align:center;line-height:40px;color:#fff}

/* footer */
.footer{left:0;top:2890px;width:1200px;height:265px;background:var(--footer)}
.f-head{top:2920px;color:#fff;font-size:11px;text-transform:uppercase;font-weight:600;padding-bottom:8px;border-bottom:2px solid var(--accent)}
.f-text{font-size:10.5px;line-height:18px;color:var(--footer-text)}
.f-brand{left:160px;top:2978px;display:flex;align-items:center;gap:10px;color:#fff;font-family:"Roboto Condensed",sans-serif;font-weight:700;font-size:26px}
.f-brand i{width:26px;height:26px;background:#888;display:block}
.f-icon{width:30px;height:30px;border-radius:50%;border:1px solid #666;display:flex;align-items:center;justify-content:center}
.f-list{list-style:none;font-size:10.5px;line-height:29px;color:var(--footer-text)}
.f-list li::before{content:"";display:inline-block;width:4px;height:4px;border-radius:50%;background:#888;margin-right:14px;vertical-align:middle}
.copyright{left:0;top:3155px;width:1200px;height:54px;background:var(--footer-deep);color:var(--footer-text);font-size:10.5px;text-align:center;line-height:54px}
</style>
</head>
<body>
<div class="page">

  <!-- hero -->
  <section class="abs hero"></section>
  <div class="abs hero-visual" role="img" aria-label="Photo of a hand holding a smartphone showing the app"></div>
  <div class="abs topbar"></div>
  <span class="abs social" style="left:167px"></span>
  <span class="abs social" style="left:186px"></span>
  <span class="abs social" style="left:205px"></span>
  <span class="abs social" style="left:224px"></span>
  <span class="abs topbar-info" style="left:845px">&#9993;&nbsp; Email Us</span>
  <span class="abs topbar-info" style="left:922px">&#9742;&nbsp; (555) 014 220 7361</span>

  <div class="abs brand"><i class="brand-mark"></i>KOVRIX</div>
  <nav class="abs nav">
    <span class="active">Home</span><span>About</span><span>Services</span><span>Portfolio</span><span>Facts</span><span>Blogs</span><span>Contact</span>
  </nav>

  <div class="abs hero-kicker">WE DEVELOP AWESOME</div>
  <div class="abs hero-title">MOBILE APP</div>
  <div class="abs read-more">Read More</div>
  <span class="abs slide-dot" style="top:266px"></span>
  <span class="abs slide-dot" style="top:282px"></span>
  <span class="abs slide-dot" style="top:298px;background:var(--accent);border-color:var(--accent)"></span>
  <span class="abs slide-dot" style="top:314px"></span>

  <!-- services -->
  <h2 class="abs section-title" style="top:608px">What we love yo do?</h2>
  <svg class="abs divider" style="top:652px" viewBox="0 0 110 10"><line x1="0" y1="5" x2="45" y2="5" stroke="#999"/><line x1="65" y1="5" x2="110" y2="5" stroke="#999"/><path d="M55 1v8M51 5h8" stroke="#999"/></svg>

  <div class="abs service" style="left:160px;top:702px">
    <h3>Web Design</h3>
    <svg width="44" height="44" viewBox="0 0 44 44"><path d="M8 36L32 8l5 5-24 28-7 2z" fill="none" stroke="#444" stroke-width="3"/><path d="M8 8l28 28" stroke="#444" stroke-width="4"/></svg>
    <p>Praesent quis porta justo. Cras vestibulum lectus luctus, maximus massa a, tristique erat.</p>
  </div>
  <div class="abs service featured" style="left:460px;top:702px">
    <h3>Web Development</h3>
    <svg width="50" height="44" viewBox="0 0 50 44"><path d="M14 10L3 22l11 12M36 10l11 12-11 12M29 6L21 38" fill="none" stroke="#fff" stroke-width="3"/></svg>
    <p>Praesent quis porta justo. Cras vestibulum lectus luctus, maximus massa a, tristique erat.</p>
  </div>
  <div class="abs service" style="left:761px;top:702px">
    <h3>Mobile App Development</h3>
    <svg width="44" height="44" viewBox="0 0 44 44"><rect x="10" y="4" width="22" height="36" rx="3" fill="none" stroke="#444" stroke-width="3"/><circle cx="22" cy="22" r="6" fill="none" stroke="#444" stroke-width="3"/></svg>
    <p>Praesent quis porta justo. Cras vestibulum lectus luctus, maximus massa a, tristique erat.</p>
  </div>
  <div class="abs service" style="left:160px;top:886px">
    <h3>Route Planning</h3>
    <svg width="44" height="44" viewBox="0 0 44 44"><g stroke="#444" stroke-width="2"><line x1="22" y1="22" x2="8" y2="8"/><line x1="22" y1="22" x2="38" y2="12"/><line x1="22" y1="22" x2="10" y2="38"/><line x1="22" y1="22" x2="36" y2="36"/></g><g fill="#444"><circle cx="22" cy="22" r="5"/><circle cx="8" cy="8" r="4"/><circle cx="38" cy="12" r="4"/><circle cx="10" cy="38" r="4"/><circle cx="36" cy="36" r="4"/></g></svg>
    <p>Praesent quis porta justo. Cras vestibulum lectus luctus, maximus massa a, tristique erat.</p>
  </div>
  <div class="abs service" style="left:460px;top:886px">
    <h3>Enterprise App Development</h3>
    <svg width="44" height="44" viewBox="0 0 44 44"><circle cx="18" cy="24" r="10" fill="none" stroke="#444" stroke-width="6" stroke-dasharray="5 3"/><circle cx="34" cy="10" r="6" fill="none" stroke="#444" stroke-width="4" stroke-dasharray="3 2"/></svg>
    <p>Praesent quis porta justo. Cras vestibulum lectus luctus, maximus massa a, tristique erat.</p>
  </div>
  <div class="abs service" style="left:761px;top:886px">
    <h3>Corporate Level App</h3>
    <svg width="44" height="44" viewBox="0 0 44 44"><rect x="10" y="4" width="22" height="36" rx="3" fill="none" stroke="#444" stroke-width="3"/><circle cx="22" cy="22" r="7" fill="none" stroke="#444" stroke-width="4" stroke-dasharray="4 2"/></svg>
    <p>Praesent quis porta justo. Cras vestibulum lectus luctus, maximus massa a, tristique erat.</p>
  </div>

  <!-- about -->
  <h2 class="abs section-title" style="top:1078px">Know about us</h2>
  <svg class="abs divider" style="top:1120px" viewBox="0 0 110 10"><line x1="0" y1="5" x2="45" y2="5" stroke="#999"/><line x1="65" y1="5" x2="110" y2="5" stroke="#999"/><path d="M55 1v8M51 5h8" stroke="#999"/></svg>

  <div class="abs video" role="img" aria-label="Video still of a team meeting around a table"></div>
  <svg class="abs" style="left:356px;top:1282px" width="38" height="38" viewBox="0 0 38 38"><circle cx="19" cy="19" r="17" fill="none" stroke="#fff" stroke-width="2"/><rect x="13" y="11" width="4" height="16" fill="#fff"/><rect x="21" y="11" width="4" height="16" fill="#fff"/></svg>
  <span class="abs" style="left:168px;top:1378px;color:#fff;font-size:10px">2:16</span>
  <div class="abs" style="left:210px;top:1386px;width:330px;height:3px;background:rgba(255,255,255,.5)"></div>
  <div class="abs" style="left:210px;top:1386px;width:132px;height:3px;background:#fff"></div>
  <span class="abs" style="left:334px;top:1378px;width:18px;height:18px;border-radius:50%;background:#fff"></span>
  <span class="abs" style="left:560px;top:1378px;color:#fff;font-size:10px">5:41</span>

  <p class="abs about-lead">Praesent quis porta justo. Cras vestibulum lectus luctus,</p>
  <p class="abs about-text" style="top:1216px">In elementum, quam nec fermentum sodales, lectus neque pulvinar diam, vulputate sagittis ipsum enim ac arcu. In hac habitasse platea dictumst. Praesent blandit nulla nec mauris elementum, vitae pulvinar augue interdum. Nam ut congue urna, sit amet pretium sem.</p>
  <p class="abs about-text about-item" style="top:1305px">Class aptent taciti sociosqu ad litora torquent per conubia nostra, per inceptos himenaeos. Nulla auctor ipsum ac augue congue, in mattis mi faucibus. Praesent eget accumsan neque.</p>
  <p class="abs about-text about-item" style="top:1370px">Nam pellentesque sed sapien non consectetur. Donec vel molestie lectus, id elementum enim. Duis et ullamcorper augue. Donec molestie erat id quam eleifend accumsan.</p>

  <!-- stats -->
  <section class="abs stats" role="img" aria-label="Dim office photograph behind the figures"></section>
  <div class="abs stat" style="left:173px;top:1506px"><div class="stat-ring"><b>400+</b></div><div class="stat-label">Team Strength</div></div>
  <div class="abs stat" style="left:396px;top:1506px"><div class="stat-ring"><b>100+</b></div><div class="stat-label">Clients Worked With</div></div>
  <div class="abs stat" style="left:620px;top:1506px"><div class="stat-ring"><b>200+</b></div><div class="stat-label">Completed Projects</div></div>
  <div class="abs stat" style="left:845px;top:1506px"><div class="stat-ring"><b>50+</b></div><div class="stat-label">Ongoing Projects</div></div>

  <!-- process -->
  <h2 class="abs section-title" style="top:1731px">Our work process</h2>
  <svg class="abs divider" style="top:1773px" viewBox="0 0 110 10"><line x1="0" y1="5" x2="45" y2="5" stroke="#999"/><line x1="65" y1="5" x2="110" y2="5" stroke="#999"/><path d="M55 1v8M51 5h8" stroke="#999"/></svg>
  <div class="abs process-line"></div>
  <div class="abs step current" style="left:201px;top:1840px"><div class="step-circle">1</div><div class="step-label">Idea</div></div>
  <div class="abs step" style="left:426px;top:1840px"><div class="step-circle">2</div><div class="step-label">Planning</div></div>
  <div class="abs step" style="left:652px;top:1840px"><div class="step-circle">3</div><div class="step-label">Design</div></div>
  <div class="abs step" style="left:875px;top:1840px"><div class="step-circle">4</div><div class="step-label">Develop</div></div>

  <!-- testimonial -->
  <div class="abs testimonial-photo" role="img" aria-label="Greyscale photo of colleagues in an office"></div>
  <div class="abs testimonial-frame">
    <h2>What our client say’s</h2>
    <p>There are many variations of passages of Lorem Ipsum available, but the majority have suffered alteration in some form, by injected humour, or randomised words which don't look even slightly believable.</p>
  </div>
  <div class="abs testimonial-side"></div>
  <div class="abs avatar" role="img" aria-label="Client portrait"></div>
  <p class="abs quote">Lorem Ipsum is simply dummy text of the printing and typesetting industry. Lorem Ipsum has been the industry's standard dummy text ever since the 1500s, when an unknown printer took a galley of type and scrambled it to make a type specimen book.. It has survived not only</p>
  <p class="abs quote-author">- Dorian Kell CEO Tallmark</p>
  <span class="abs bullet" style="left:856px;top:2329px"></span>
  <span class="abs bullet" style="left:876px;top:2329px"></span>
  <span class="abs bullet" style="left:896px;top:2329px;background:var(--accent)"></span>

  <!-- clients -->
  <h2 class="abs section-title" style="top:2486px">Our clients</h2>
  <svg class="abs divider" style="top:2528px" viewBox="0 0 110 10"><line x1="0" y1="5" x2="45" y2="5" stroke="#999"/><line x1="65" y1="5" x2="110" y2="5" stroke="#999"/><path d="M55 1v8M51 5h8" stroke="#999"/></svg>
  <div class="abs client" style="left:137px"><i></i>COMPANY</div>
  <div class="abs client" style="left:336px"><i></i>company</div>
  <div class="abs client" style="left:530px"><i></i>COMPANY</div>
  <div class="abs client" style="left:725px"><i></i>CompanyName</div>
  <div class="abs client" style="left:906px"><i></i>COMPANYNAME</div>
  <span class="abs bullet" style="left:580px;top:2688px;background:#999"></span>
  <span class="abs bullet" style="left:600px;top:2688px;background:var(--accent)"></span>

  <!-- newsletter -->
  <section class="abs newsletter"></section>
  <div class="abs nl-title">Suscribe our newsletter</div>
  <div class="abs nl-sub">Get notified about the latest updates.</div>
  <div class="abs nl-input">Your email address</div>
  <div class="abs nl-button">Suscribe</div>

  <!-- footer -->
  <footer class="abs footer"></footer>
  <div class="abs f-head" style="left:160px">About us</div>
  <div class="abs f-brand"><i></i>KOVRIX</div>
  <p class="abs f-text" style="left:160px;top:3040px;width:270px">Kovrix Group, works as international construction services company and is a leading builder in diverse and numerous market segments. Lorem ipsum dolor sit amet, consectetur adipiscing elit.</p>

  <div class="abs f-head" style="left:462px">Contacts</div>
  <div class="abs f-icon" style="left:462px;top:2968px"><svg width="12" height="14" viewBox="0 0 12 14"><path d="M6 13S1 7.5 1 5a5 5 0 0110 0c0 2.5-5 8-5 8z" fill="none" stroke="#aaa"/><circle cx="6" cy="5" r="1.6" fill="#aaa"/></svg></div>
  <p class="abs f-text" style="left:500px;top:2966px">PO Box 40917, Harrow Lane East,<br>Westvale 5512.<br>United States.</p>
  <div class="abs f-icon" style="left:462px;top:3038px"><svg width="12" height="12" viewBox="0 0 12 12"><path d="M2 1h3l1 3-2 1a6 6 0 003 3l1-2 3 1v3c-6 0-10-4-10-10z" fill="#aaa"/></svg></div>
  <p class="abs f-text" style="left:500px;top:3044px">(555) 014 220 7361</p>
  <div class="abs f-icon" style="left:462px;top:3090px"><svg width="12" height="10" viewBox="0 0 12 10"><rect x=".5" y=".5" width="11" height="9" fill="none" stroke="#aaa"/><path d="M.5 .5L6 5l5.5-4.5" fill="none" stroke="#aaa"/></svg></div>
  <p class="abs f-text" style="left:500px;top:3096px">info@example.com</p>

  <div class="abs f-head" style="left:761px">Infomations</div>
  <ul class="abs f-list" style="left:778px;top:2966px"><li>Home</li><li>Company</li><li>Certifications</li><li>Company</li><li>Core Values</li></ul>
  <ul class="abs f-list" style="left:909px;top:2966px"><li>Faq</li><li>Manuals</li><li>Company History</li><li>Locations</li><li>Privacy</li></ul>

  <div class="abs copyright">Copyright © 2016 Kovrix Solutions. All right reserved.</div>
</div>
</body>
</html>
```